Flyer Design for legal services company - front and back A6

Hi all!

We are a legal services company looking to create some flyers for local advertising.

We need a flyer designed to hand out to local law firms and prospective clients. It will most likely be the attorney or paralegal reading and receiving the flyer. Make sure it looks very professional.

Also, we will be using the spot gloss printing on most of the gold accents in the flyer, like our logo, so keep that in mind while designing.

Here are some lines of copy you can include in the flyer:
"Professional servers on staff"
"Continuous status updates via email and online portal"*
"Dedicated account manager"*
"Jobs start immediately"
"Personalized, professional service"
"Rush and same-day service"

Here is our info
Company name: Brightwell Serve
Phone: (418) 639-2157

Attached are JPG files of our logo in different colors and a stock photo for use in the flyer. Use "Anton" and/or "DIN Next Light" for fonts. Check our website [login to view URL] for our current design theme.

Flyer size: A6 4.1in. x 5.8in.
Front and Back please!

Looking forward to seeing your work!

```html
<!DOCTYPE html>
<html lang="en">
<head>
<meta charset="utf-8">
<title>Brightwell Serve – Flyer Front and Back</title>
<link rel="stylesheet" href="https://fonts.googleapis.com/css2?family=Anton&family=Barlow+Condensed:wght@300;400;600&family=Barlow:wght@400;600&display=swap">
<style>
  :root {
    --backdrop: #e3e5e6;
    --navy: #283572;
    --navy-deep: #222c63;
    --band-blue: #2e4180;
    --gold: #cdac52;
    --gold-soft: #e6cf7a;
    --gray-bar: #8a8387;
    --white: #ffffff;
    --cream: #f3ead0;
    --rule: rgba(255,255,255,0.55);
  }
  * { margin: 0; padding: 0; box-sizing: border-box; }
  html, body { width: 1200px; height: 880px; overflow: hidden; background: var(--backdrop); }
  .canvas { position: relative; width: 1200px; height: 880px; }

  .flyer { position: absolute; background: var(--navy); overflow: hidden; }
  .flyer-front { left: 163px; top: 143px; width: 418px; height: 582px; }
  .flyer-back  { left: 631px; top: 143px; width: 422px; height: 588px; }

  .brand { position: absolute; left: 0; right: 0; display: flex; flex-direction: column; align-items: center; }
  .brand-square { background: var(--gold); }
  .brand-name {
    font-family: "Barlow Condensed", sans-serif; font-weight: 400;
    color: var(--gold); text-transform: uppercase; letter-spacing: 2px; white-space: nowrap;
  }
  .flyer-front .brand { top: 22px; }
  .flyer-front .brand-square { width: 40px; height: 40px; margin-bottom: 14px; }
  .flyer-front .brand-name { font-size: 15px; }
  .flyer-back .brand { top: 54px; }
  .flyer-back .brand-square { width: 56px; height: 56px; margin-bottom: 20px; }
  .flyer-back .brand-name { font-size: 19px; }

  .art { position: absolute; left: 0; width: 100%; }
  .flyer-front .art { top: 0; height: 582px; }
  .flyer-back .art { top: 0; height: 588px; }

  .title-frame {
    position: absolute; left: 73px; top: 231px; width: 274px; height: 129px;
    border: 1.5px solid var(--gold);
  }
  .title-panel {
    position: absolute; left: 80px; top: 255px; width: 256px; height: 69px;
    background: rgba(120,112,130,0.72);
    display: flex; flex-direction: column; align-items: center; justify-content: center; gap: 4px;
  }
  .title-name {
    font-family: "Barlow Condensed", sans-serif; font-weight: 600;
    font-size: 23px; color: var(--white); letter-spacing: 1px; text-transform: uppercase;
  }
  .title-tagline {
    font-family: "Barlow Condensed", sans-serif; font-weight: 300;
    font-size: 15px; color: var(--white); letter-spacing: 0.5px; text-transform: uppercase;
  }

  .contact-band { position: absolute; left: 0; top: 460px; width: 100%; height: 122px; background: var(--band-blue); }
  .contact-heading {
    position: absolute; top: 17px; width: 100%; text-align: center;
    font-family: "Anton", sans-serif; font-size: 19px; color: var(--white); letter-spacing: 4px;
  }
  .contact-rule { position: absolute; left: 19px; right: 21px; height: 1px; background: var(--rule); }
  .contact-rule.top { top: 51px; }
  .contact-rule.bottom { top: 95px; }
  .contact-grid {
    position: absolute; top: 59px; left: 0; width: 100%;
    display: grid; grid-template-columns: 175px 12px 12px 1fr; row-gap: 5px; column-gap: 0;
    font-family: "Barlow", sans-serif; font-size: 10px; color: var(--white); line-height: 11px;
  }
  .contact-grid .left { text-align: right; padding-right: 8px; }
  .contact-grid .right { padding-left: 6px; }
  .marker { width: 9px; height: 9px; background: var(--gold-soft); margin-top: 1px; }
  .marker.second { margin-left: 20px; }
  .contact-grid .right { margin-left: 22px; }

  .services-label {
    position: absolute; left: 60px; top: 281px; width: 44px; height: 272px;
    background: var(--gray-bar); display: flex; align-items: center; justify-content: center;
  }
  .services-label span {
    display: block; transform: rotate(-90deg); white-space: nowrap;
    font-family: "Anton", sans-serif; font-size: 18px; color: var(--white); letter-spacing: 1.5px;
  }
  .service-list {
    position: absolute; left: 145px; top: 410px; width: 250px; list-style: none;
    font-family: "Barlow", sans-serif; font-weight: 600; font-size: 9.5px; color: var(--cream); line-height: 18px;
  }
  .service-list li { position: relative; padding-left: 19px; }
  .service-list li::before {
    content: ""; position: absolute; left: 0; top: 4px; width: 10px; height: 10px; border-radius: 50%;
    background: var(--gold); box-shadow: inset 0 0 0 2px #e8d38a;
  }
</style>
</head>
<body>
<main class="canvas">

  <section class="flyer flyer-front" aria-label="Flyer front">
    <svg class="art" viewBox="0 0 418 582" preserveAspectRatio="none">
      <defs>
        <linearGradient id="front-city" x1="0" y1="0" x2="1" y2="1">
          <stop offset="0" stop-color="#6e4f7e"/>
          <stop offset="0.45" stop-color="#b6a4a8"/>
          <stop offset="0.7" stop-color="#e7e0c2"/>
          <stop offset="1" stop-color="#8d6f88"/>
        </linearGradient>
      </defs>
      <rect x="0" y="115" width="418" height="345" fill="var(--navy-deep)"/>
      <polygon points="0,150 40,115 300,115 418,230 418,460 150,460 0,320" fill="url(#front-city)" role="img" aria-label="Photo looking up at city skyscrapers"/>
      <line x1="250" y1="115" x2="418" y2="280" stroke="var(--gold)" stroke-width="2"/>
      <line x1="0" y1="250" x2="110" y2="460" stroke="var(--gold)" stroke-width="2"/>
    </svg>
    <div class="brand">
      <div class="brand-square"></div>
      <div class="brand-name">Brightwell Serve</div>
    </div>
    <div class="title-frame"></div>
    <div class="title-panel">
      <div class="title-name">Brightwell Serve</div>
      <div class="title-tagline">National Attorney Services</div>
    </div>
    <div class="contact-band">
      <h2 class="contact-heading">CONTACT US</h2>
      <div class="contact-rule top"></div>
      <div class="contact-grid">
        <span class="left">Brightwell Serve</span><span class="marker"></span><span class="marker second"></span><span class="right">email: info@brightwellserve.com</span>
        <span class="left">Phone: (418) 639-2157</span><span class="marker"></span><span class="marker second"></span><span class="right">website: www.brightwellserve.com</span>
      </div>
      <div class="contact-rule bottom"></div>
    </div>
  </section>

  <section class="flyer flyer-back" aria-label="Flyer back">
    <svg class="art" viewBox="0 0 422 588" preserveAspectRatio="none">
      <defs>
        <linearGradient id="back-city" x1="0" y1="1" x2="1" y2="0">
          <stop offset="0" stop-color="#6a4f78"/>
          <stop offset="0.5" stop-color="#c9b9a6"/>
          <stop offset="0.75" stop-color="#efe9c6"/>
          <stop offset="1" stop-color="#9a7f86"/>
        </linearGradient>
      </defs>
      <polygon points="0,284 103,191 422,191 422,284 323,373 0,373" fill="url(#back-city)" role="img" aria-label="Photo looking up at city skyscrapers"/>
      <line x1="88" y1="191" x2="0" y2="270" stroke="var(--gold)" stroke-width="3"/>
      <line x1="422" y1="300" x2="340" y2="373" stroke="var(--gold)" stroke-width="3"/>
    </svg>
    <div class="brand">
      <div class="brand-square"></div>
      <div class="brand-name">Brightwell Serve</div>
    </div>
    <div class="services-label"><span>WHAT WE CAN DO FOR YOU</span></div>
    <ul class="service-list">
      <li>Professional servers on staff</li>
      <li>Continuous status updates via email<br>and online portal</li>
      <li>Dedicated account manager</li>
      <li>Jobs start immediately</li>
      <li>Personalized, professional service</li>
      <li>Rush and same-day service</li>
    </ul>
  </section>

</main>
</body>
</html>
```